Business Card Design

I have a very clear idea of what I want. I just do not know how to do the graphic design to match it.

On the front I want the uploaded image with the horse and the two people.
I want

Bottom left hand corner
Lewis Brand
0438 512 607

Bottom right
There is maroon block with Neil Patton Practitioner Group Logo
Next to that I want the Stable Arc tile about the same size ( attached psd file)

On the back I want a plain colour (white) with the information

Lewis Brand
Equine Performance
Rowland4Ponies and Acupuncture
Horsemanship Lessons and Clinics
Horse Training

lbrand@fauna812.com.au
FB/lewis.brand.207
StableArc.com.au

Industry/Entity Type

Business

Contact Information for Business Card

Lewis Brand
0438 512 607
lbrand@fauna812.com.au

```html
<!DOCTYPE html>
<html lang="en">
<head>
<meta charset="utf-8">
<title>Lewis Brand – Business Card</title>
<link rel="stylesheet" href="https://fonts.googleapis.com/css2?family=Tinos:wght@400;700&family=Cinzel:wght@400&family=Allura&display=swap">
<style>
  :root {
    --page-bg: #e9e6e3;
    --card-white: #ffffff;
    --ink: #1c1a19;
    --maroon: #8a1c12;
    --brown: #4a2a1c;
    --tile-maroon: #7a2f1f;
    --tile-cream: #f4efe6;
    --sand-light: #dcc8a0;
    --sand-mid: #c6aa7c;
    --sand-dark: #9c8158;
    --subject-dark: #6f5a40;
    --shadow: 0 10px 30px rgba(0,0,0,.18);
  }
  * { box-sizing: border-box; margin: 0; padding: 0; }
  html, body { width: 1200px; height: 800px; overflow: hidden; }
  body {
    background: var(--page-bg);
    font-family: "Tinos", "Times New Roman", serif;
    color: var(--ink);
    position: relative;
  }
  .card {
    position: absolute;
    top: 235px;
    width: 530px;
    height: 330px;
    background: var(--card-white);
    box-shadow: var(--shadow);
    overflow: hidden;
  }

  /* Back of card */
  .card-back { left: 40px; padding: 34px 36px; }
  .back-name {
    font-size: 26px;
    color: var(--maroon);
    font-weight: 400;
    line-height: 1.1;
  }
  .services { list-style: none; margin-top: 4px; margin-left: 10px; }
  .services li { font-size: 15px; line-height: 1.2; }
  .back-contacts {
    position: absolute;
    left: 250px;
    bottom: 34px;
    list-style: none;
  }
  .back-contacts li {
    font-size: 16px;
    line-height: 1.25;
    display: flex;
    align-items: center;
    gap: 7px;
  }
  .contact-icon { width: 13px; height: 13px; flex: none; }
  .contact-square { width: 12px; height: 12px; background: var(--ink); border-radius: 2px; flex: none; }

  /* Front of card */
  .card-front { left: 630px; }
  .field-photo {
    position: absolute; inset: 0;
    background: radial-gradient(ellipse at 55% 40%, var(--sand-light) 0%, var(--sand-mid) 65%, var(--sand-dark) 100%);
  }
  .photo-subjects {
    position: absolute;
    left: 150px; top: 140px;
    width: 380px; height: 190px;
    background: radial-gradient(ellipse at 60% 55%, rgba(111,90,64,.55) 0%, rgba(111,90,64,.25) 45%, rgba(111,90,64,0) 75%);
  }
  .headline {
    position: absolute; left: 0; top: 0;
    width: 530px; height: 205px;
  }
  .headline .arc-text {
    font-family: "Cinzel", "Times New Roman", serif;
    font-size: 16px;
    letter-spacing: 1px;
    fill: var(--brown);
  }
  .headline .script-small {
    font-family: "Allura", cursive;
    font-size: 32px;
    fill: var(--brown);
  }
  .headline .script-large {
    font-family: "Allura", cursive;
    font-size: 92px;
    fill: var(--brown);
  }
  .headline .swash { fill: none; stroke: var(--brown); stroke-width: 2; }

  .contact-panel {
    position: absolute;
    left: 12px; top: 208px;
    width: 410px; height: 110px;
    background: var(--card-white);
    border-radius: 12px;
    box-shadow: 0 2px 6px rgba(0,0,0,.2);
    padding: 12px 18px;
  }
  .front-name { font-size: 24px; font-weight: 700; line-height: 1.1; }
  .front-phone { font-size: 15px; display: flex; align-items: center; gap: 6px; }
  .phone-icon { width: 12px; height: 12px; }

  .tile-stable-arc {
    position: absolute;
    left: 352px; top: 256px;
    width: 54px; height: 54px;
    background: var(--tile-cream);
    border: 3px solid var(--tile-maroon);
    border-radius: 8px;
    display: flex; align-items: center; justify-content: center;
    text-align: center;
    font-size: 10px; line-height: 1.1;
    color: var(--brown);
  }
  .tile-practitioner {
    position: absolute;
    left: 440px; top: 244px;
    width: 72px; height: 72px;
    background: var(--tile-maroon);
    display: flex; align-items: center; justify-content: center;
    text-align: center;
    padding: 4px;
    font-size: 10px; line-height: 1.15;
    color: #f1c9a8;
  }
</style>
</head>
<body>

  <section class="card card-back" aria-label="Back of business card">
    <h1 class="back-name">Lewis Brand</h1>
    <ul class="services">
      <li>Equine Performance</li>
      <li>Rowland4Ponies and Acupuncture</li>
      <li>Horsemanship Lessons and Clinics</li>
      <li>Horse Training</li>
    </ul>
    <ul class="back-contacts">
      <li>
        <svg class="contact-icon" viewBox="0 0 13 13" aria-hidden="true">
          <rect x="0" y="0" width="13" height="13" rx="2" fill="#1c1a19"/>
          <rect x="2" y="3.5" width="9" height="6" fill="none" stroke="#fff" stroke-width="1"/>
          <polyline points="2,3.5 6.5,7 11,3.5" fill="none" stroke="#fff" stroke-width="1"/>
        </svg>
        lbrand@fauna812.com.au
      </li>
      <li><span class="contact-square"></span>lewis.brand.207</li>
      <li><span class="contact-square"></span>www.stablearc.com.au</li>
    </ul>
  </section>

  <section class="card card-front" aria-label="Front of business card">
    <div class="field-photo" role="img" aria-label="Sandy arena background of the photograph"></div>
    <div class="photo-subjects" role="img" aria-label="Photograph of a man and a woman working a bay horse on a lead rope in the arena"></div>

    <svg class="headline" viewBox="0 0 530 205" aria-label="How you ever gonna know your potential">
      <defs>
        <path id="headline-arc" d="M 70 72 Q 280 0 490 100"/>
      </defs>
      <text class="arc-text"><textPath href="#headline-arc" startOffset="4">HOW YOU EVER GONNA KNOW</textPath></text>
      <path class="swash" d="M 60 84 Q 285 10 500 112"/>
      <text class="script-small" x="318" y="112">Your</text>
      <text class="script-large" x="70" y="172">Potential</text>
    </svg>

    <div class="contact-panel">
      <p class="front-name">Lewis Brand</p>
      <p class="front-phone">
        <svg class="phone-icon" viewBox="0 0 12 12" aria-hidden="true">
          <path d="M1 3 Q1 1 3 1 L9 1 Q11 1 11 3 L10 4 L8 4 L8 3 L4 3 L4 4 L2 4 Z M2 5 L10 5 L11 11 L1 11 Z" fill="#1c1a19"/>
        </svg>
        0438 512 607
      </p>
    </div>

    <div class="tile-stable-arc">Stable Arc</div>
    <div class="tile-practitioner">Neil Patton Practitioner Group</div>
  </section>

</body>
</html>
```